New Business Card for Casual Beachfront Cafe

Quirky Beachfront Cafe at Moana, South Australia needs a DOUBLE SIDED business card to print on PrintHarbor.

Target Market(s)

Business Cards sit on the counter for Guests to take with them. Please view our website www.saltreefcafe.com.au to get a feel for the Cafe. You may also view our Instagram at @saltreefcafe

Industry/Entity Type

Cafe / Restaurant

Contact Information for Business Card

Information equivalent to: Breakfast, Lunch, Dinner, Coffee, Takeaway / 117 Parade Shellhaven SA 5190 / Menu & Opening Hours: www.saltreefcafe.com.au / ph (08) 8461 9273

Requirements
Must have
• Information equivalent to: Breakfast, Lunch, Dinner, Coffee, Takeaway / 117 Parade Shellhaven SA 5190 / Menu & Opening Hours: www.saltreefcafe.com.au / ph (08) 8461 9273
Nice to have
• Potentially some of our trademark colours (Cafe can be searched via Seekly)
Should not have
• Must NOT have image of the building. May have the logo provided on one side but not necessarily, depending on how you wish to design the card

```html
<!DOCTYPE html>
<html lang="en">
<head>
<meta charset="utf-8">
<title>Salt Reef Cafe – Business Card</title>
<link href="https://fonts.googleapis.com/css2?family=Poppins:wght@400;500;700;800&display=swap" rel="stylesheet">
<style>
  :root {
    --backdrop: #2d2d2d;
    --card: #000000;
    --yellow: #ffff1a;
    --navy: #123a78;
    --rust: #b4560f;
    --white: #ffffff;
  }
  * { box-sizing: border-box; margin: 0; padding: 0; }
  html, body {
    width: 1200px; height: 1015px; overflow: hidden;
    background: var(--backdrop);
    font-family: "Poppins", sans-serif;
  }
  .canvas { position: relative; width: 1200px; height: 1015px; }
  .card {
    position: absolute; left: 190px; width: 820px; height: 460px;
    background: var(--card);
    box-shadow: 0 14px 30px rgba(0,0,0,.45);
    overflow: hidden;
  }
  .card--hours { top: 34px; }
  .card--contact { top: 522px; }

  /* Hours side */
  .hours-label {
    position: absolute; left: 62px; top: 230px;
    transform: translate(-50%, -50%) rotate(-90deg);
    color: var(--yellow); font-weight: 500; font-size: 20px; letter-spacing: .5px;
    white-space: nowrap;
  }
  .timeline { position: absolute; left: 0; top: 0; }
  .hours-row { position: absolute; left: 175px; display: flex; }
  .hours-row .day {
    width: 125px; color: var(--yellow); font-weight: 800; font-size: 21px;
  }
  .hours-row .time {
    color: var(--white); font-size: 21px; line-height: 30px; letter-spacing: .5px;
  }
  .service-box {
    position: absolute; left: 470px; top: 78px; width: 310px; height: 170px;
    background: var(--yellow); border: 6px solid var(--rust);
    display: flex; flex-direction: column; align-items: center; justify-content: center;
    color: var(--navy); font-weight: 800; font-size: 21px; line-height: 1.45;
    text-align: center; letter-spacing: .5px;
  }
  .service-box .sep { color: var(--rust); padding: 0 6px; }

  /* Contact side */
  .contact-line {
    position: absolute; left: 60px; display: flex; align-items: center; gap: 18px;
    color: var(--white); font-weight: 500; font-size: 28px; line-height: 1.15;
  }
  .contact-line--address { top: 130px; font-size: 29px; }
  .contact-line--phone { top: 318px; font-size: 32px; }
  .contact-line--web { top: 382px; font-size: 30px; }
  .contact-line svg { flex: none; }
  .brand-box {
    position: absolute; left: 468px; top: 55px; width: 320px; height: 200px;
    background: var(--yellow); border: 6px solid var(--rust);
    display: flex; flex-direction: column; align-items: center; justify-content: center;
    color: var(--navy); font-weight: 800; font-size: 46px; line-height: 1.05;
    text-align: center; text-transform: uppercase;
  }
</style>
</head>
<body>
<main class="canvas">

  <section class="card card--hours" aria-label="Opening hours side">
    <div class="hours-label">OPENING HOURS</div>
    <svg class="timeline" width="820" height="460" aria-hidden="true">
      <line x1="130" y1="40" x2="130" y2="430" stroke="var(--yellow)" stroke-width="1.5"/>
      <g fill="var(--card)" stroke="var(--yellow)" stroke-width="1.5">
        <circle cx="130" cy="125" r="12"/>
        <circle cx="130" cy="235" r="12"/>
        <circle cx="130" cy="365" r="12"/>
      </g>
      <g fill="var(--navy)">
        <circle cx="130" cy="125" r="4"/>
        <circle cx="130" cy="235" r="4"/>
        <circle cx="130" cy="365" r="4"/>
      </g>
    </svg>
    <div class="hours-row" style="top:60px"><span class="day">Mon</span><span class="time">Closed</span></div>
    <div class="hours-row" style="top:92px"><span class="day">Tues</span><span class="time">Closed</span></div>
    <div class="hours-row" style="top:136px"><span class="day">Wed</span><span class="time">9am–2pm<br>5pm–8pm</span></div>
    <div class="hours-row" style="top:204px"><span class="day">Thur</span><span class="time">9am–2pm<br>5pm–8pm</span></div>
    <div class="hours-row" style="top:272px"><span class="day">Fri</span><span class="time">9am–2pm<br>5pm–8pm</span></div>
    <div class="hours-row" style="top:348px"><span class="day">Sat</span><span class="time">8:30am–8pm</span></div>
    <div class="hours-row" style="top:380px"><span class="day">Sun</span><span class="time">8:30am–8pm</span></div>

    <div class="service-box">
      <span>BREAKFAST<span class="sep">•</span>LUNCH</span>
      <span>DINNER<span class="sep">•</span>COFFEE</span>
      <span>TAKEAWAY</span>
    </div>
  </section>

  <section class="card card--contact" aria-label="Contact side">
    <div class="brand-box"><span>Salt Reef</span><span>Cafe</span></div>

    <div class="contact-line contact-line--address">
      <svg width="50" height="50" viewBox="0 0 50 50" aria-hidden="true">
        <circle cx="25" cy="25" r="22" fill="none" stroke="var(--yellow)" stroke-width="2.5"/>
        <path d="M25 13a8 8 0 0 0-8 8c0 6 8 15 8 15s8-9 8-15a8 8 0 0 0-8-8z" fill="var(--yellow)"/>
        <circle cx="25" cy="21" r="3" fill="var(--card)"/>
      </svg>
      <span>117 Parade<br>Shellhaven SA 5190</span>
    </div>

    <div class="contact-line contact-line--phone">
      <svg width="50" height="50" viewBox="0 0 50 50" aria-hidden="true">
        <circle cx="25" cy="25" r="22" fill="none" stroke="var(--yellow)" stroke-width="2.5"/>
        <path d="M17 15l4-1 3 6-2.5 2a12 12 0 0 0 6 6l2-2.5 6 3-1 4c-10 1-18-7-17.5-17.5z" fill="none" stroke="var(--yellow)" stroke-width="2" stroke-linejoin="round"/>
      </svg>
      <span>(08) 8461 9273</span>
    </div>

    <div class="contact-line contact-line--web">
      <svg width="50" height="50" viewBox="0 0 50 50" aria-hidden="true">
        <circle cx="25" cy="25" r="22" fill="none" stroke="var(--yellow)" stroke-width="2.5"/>
        <g fill="none" stroke="var(--yellow)" stroke-width="1.8">
          <circle cx="25" cy="25" r="11"/>
          <ellipse cx="25" cy="25" rx="5" ry="11"/>
          <line x1="14" y1="25" x2="36" y2="25"/>
          <line x1="16" y1="19" x2="34" y2="19"/>
          <line x1="16" y1="31" x2="34" y2="31"/>
        </g>
      </svg>
      <span>www.saltreefcafe.com.au</span>
    </div>
  </section>

</main>
</body>
</html>
```